Podcast Cover Art for Inspiring Fun Show

Title: The Dave R Hour

I am looking for a simple design that includes the following:

1. Picture of me (the one I attached with the background removed) on a simple background (please refer to attachments for ideas).
2. The title done in professional lettering that is easy to read and stands out on the background

Please see attached pictures for:

1) Other podcast art I like
2) Backgrounds that I like
3) A picture of me (please edit out the background)

Target Market(s)

Anyone into personal-development, inspiring content and motivational stories.

Font styles to use
Sans Serif

Colors

Designer to choose colors to be used in the design.

Requirements
Must have
• - Title "The Dave R Hour" in professional lettering that is large and very easy to read
• - Picture of me on the background

```html
<!DOCTYPE html>
<html lang="en">
<head>
<meta charset="UTF-8">
<title>The Dave R Hour — Podcast Cover</title>
<link rel="stylesheet" href="https://fonts.googleapis.com/css2?family=Fredoka:wght@700&display=swap">
<style>
  :root {
    --bg-lavender: #be85f0;
    --title-white: #ffffff;
    --photo-dark: #3a3f4a;
    --photo-mid: #6b6470;
    --photo-skin: #d9b39e;
  }
  * { margin: 0; padding: 0; box-sizing: border-box; }
  html, body {
    width: 1200px;
    height: 1200px;
    overflow: hidden;
    background: var(--bg-lavender);
  }
  .cover {
    position: relative;
    width: 1200px;
    height: 1200px;
    background: var(--bg-lavender);
    overflow: hidden;
  }
  .show-title {
    position: absolute;
    left: 28px;
    top: 300px;
    font-family: "Fredoka", "Arial Rounded MT Bold", sans-serif;
    font-weight: 700;
    font-size: 248px;
    line-height: 212px;
    letter-spacing: -4px;
    color: var(--title-white);
    text-transform: uppercase;
  }
  .show-title span { display: block; }
  .host-photo {
    position: absolute;
    right: 0;
    top: 68px;
    width: 340px;
    height: 1132px;
  }
</style>
</head>
<body>
  <main class="cover">
    <h1 class="show-title">
      <span>The</span>
      <span>Dave R</span>
      <span>Hour</span>
    </h1>

    <svg class="host-photo" viewBox="0 0 340 1132" role="img"
         aria-label="Cut-out photo of the host, Dave R, smiling, with dark slicked-back hair, wearing a checked shirt and grey hooded jacket">
      <defs>
        <linearGradient id="hostTones" x1="0" y1="0" x2="0" y2="1">
          <stop offset="0" stop-color="var(--photo-dark)"/>
          <stop offset="0.12" stop-color="var(--photo-skin)"/>
          <stop offset="0.68" stop-color="var(--photo-skin)"/>
          <stop offset="0.78" stop-color="var(--photo-mid)"/>
          <stop offset="1" stop-color="var(--photo-dark)"/>
        </linearGradient>
      </defs>
      <path d="M340 0 L340 1132 L0 1132 C20 1020 180 880 300 830 C220 760 160 650 140 520 C120 400 90 300 90 180 C100 70 220 10 340 0 Z"
            fill="url(#hostTones)"/>
    </svg>
  </main>
</body>
</html>
```